Business Cards

I'd like help creating business cards with the full logo "Velmora Capital Partners" on the back of the card (navy background with white writing), and abbreviated logo "VCP" on the front. Would like to list name, title, phone number, email, and website listed on front of card. Would like to keep very simple. Front font Arial or similar.

```html
<!DOCTYPE html>
<html lang="en">
<head>
<meta charset="utf-8">
<title>Velmora Capital Partners — Business Cards</title>
<link href="https://fonts.googleapis.com/css2?family=Montserrat:wght@400;600;700&display=swap" rel="stylesheet">
<style>
  :root {
    --navy: #1d3769;
    --navy-deep: #1a3263;
    --steel: #8aa3d6;
    --ink: #1f1f1f;
    --paper: #ffffff;
    --backdrop: #9a9a9a;
  }
  * { box-sizing: border-box; margin: 0; padding: 0; }
  html, body { width: 1093px; height: 1200px; overflow: hidden; }
  body {
    background: var(--backdrop);
    font-family: "Montserrat", Arial, sans-serif;
    position: relative;
  }
  .card {
    position: absolute;
    left: 262px;
    border-radius: 24px;
    overflow: hidden;
  }
  .card-back {
    top: 223px;
    width: 581px;
    height: 362px;
    background: var(--navy);
  }
  .company-name {
    position: absolute;
    left: 0; right: 0;
    top: 160px;
    text-align: center;
    color: var(--steel);
    font-weight: 600;
    font-size: 34px;
    line-height: 1.2;
  }
  .card-front {
    top: 620px;
    width: 585px;
    height: 359px;
    background: var(--paper);
  }
  .company-name-front {
    position: absolute;
    left: 76px;
    top: 140px;
    width: 190px;
    height: 89px;
    display: flex;
    align-items: center;
    justify-content: center;
    text-align: center;
    color: var(--navy);
    font-weight: 700;
    font-size: 22px;
    line-height: 1.25;
  }
  .divider {
    position: absolute;
    left: 283px;
    top: 123px;
    width: 1px;
    height: 126px;
    background: var(--navy);
  }
  .details {
    position: absolute;
    left: 298px;
    top: 120px;
  }
  .person-name {
    color: var(--navy);
    font-weight: 700;
    font-size: 22px;
    line-height: 1.2;
  }
  .person-title {
    color: var(--ink);
    font-size: 13.5px;
    margin-top: 2px;
  }
  .contact-list {
    list-style: none;
    margin-top: 15px;
  }
  .contact-item {
    display: flex;
    align-items: center;
    height: 24px;
    font-size: 13px;
    color: var(--ink);
    margin-bottom: 1px;
  }
  .contact-item svg {
    width: 16px;
    height: 16px;
    margin-right: 10px;
    fill: var(--navy);
    flex: none;
  }
  .card-band {
    position: absolute;
    left: 0; right: 0; bottom: 0;
    height: 15px;
    background: var(--navy-deep);
  }
</style>
</head>
<body>
  <section class="card card-back" aria-label="Card back">
    <p class="company-name">Velmora Capital Partners</p>
  </section>

  <section class="card card-front" aria-label="Card front">
    <p class="company-name-front">Velmora Capital Partners</p>
    <div class="divider"></div>
    <div class="details">
      <h1 class="person-name">Dorian Hale</h1>
      <p class="person-title">Managing Director</p>
      <ul class="contact-list">
        <li class="contact-item">
          <svg viewBox="0 0 16 16" aria-hidden="true"><path d="M1 6c0-2 3-3 7-3s7 1 7 3v1.5h-3.5V6h-7v1.5H1z"/><path d="M4 8h8l1.5 6h-11z"/></svg>
          877-555-0142
        </li>
        <li class="contact-item">
          <svg viewBox="0 0 16 16" aria-hidden="true"><path d="M1 4h14v1l-7 4.5L1 5z"/><path d="M1 6.5l7 4.5 7-4.5V13H1z"/></svg>
          hello@velmoracapital.com
        </li>
        <li class="contact-item">
          <svg viewBox="0 0 16 16" aria-hidden="true"><circle cx="8" cy="8" r="7"/><path d="M5 3.5c1.5.5 2 2 1 3s-2 .5-2 2 1.5 1.5 1.5 3M10 2.5c-1 1 0 2 1 2.5s2 .5 2.5 2M9.5 13c0-1.5 1-2.5 2.5-2.5" stroke="#fff" stroke-width="1.2" fill="none"/></svg>
          www.velmoracapital.com
        </li>
      </ul>
    </div>
    <div class="card-band"></div>
  </section>
</body>
</html>
```